Letterhead for Dorian Welk

I need a letterhead based on the business card design

Industry/Entity Type

Business

Requirements
Must have
• Footer: Dorian Welk Naturopath
Shop 4123c, 46 Carrow Lane, Sydney 2000

```html
<!DOCTYPE html>
<html lang="en">
<head>
<meta charset="utf-8">
<title>Dorian Welk Naturopath – Letterhead</title>
<link href="https://fonts.googleapis.com/css2?family=Questrial&display=swap" rel="stylesheet">
<style>
  :root {
    --bg: #e2e2e2;
    --paper: #ffffff;
    --orange: #e8862a;
    --orange-soft: #ef9d50;
    --leaf-a: #f6d6b6;
    --leaf-b: #efbf92;
  }
  * { margin: 0; padding: 0; box-sizing: border-box; }
  html, body { width: 942px; height: 1200px; overflow: hidden; }
  body {
    background: var(--bg);
    font-family: "Questrial", sans-serif;
    color: var(--orange);
  }
  .letterhead {
    position: absolute;
    left: 44px; top: 0;
    width: 854px; height: 1200px;
    background: var(--paper);
    overflow: hidden;
  }
  .brand {
    position: absolute;
    left: 67px; top: 42px;
    display: flex; align-items: center; gap: 10px;
    font-size: 27px; letter-spacing: 0.5px;
    color: var(--orange);
  }
  .brand-dot {
    width: 14px; height: 14px; border-radius: 50%;
    background: var(--orange);
  }
  .credentials {
    position: absolute;
    right: 75px; top: 72px;
    text-align: right;
  }
  .credentials-name {
    font-size: 19px; font-weight: 700; letter-spacing: 0.3px;
    color: var(--orange);
    margin-bottom: 6px;
  }
  .credentials-line {
    font-size: 14.5px; line-height: 24px;
    color: var(--orange-soft);
  }
  .leaf-art {
    position: absolute;
    left: 670px; top: 695px;
    width: 184px; height: 505px;
    background: linear-gradient(160deg, var(--leaf-a), var(--leaf-b));
    border-radius: 100% 0 0 60% / 70% 0 0 30%;
    opacity: 0.85;
  }
  .footer {
    position: absolute;
    left: 67px; top: 1134px;
    display: flex;
    font-size: 11px; line-height: 18px;
    color: var(--orange-soft);
  }
  .footer-col {
    border-left: 1px solid var(--orange-soft);
    padding: 0 14px 0 8px;
  }
  .footer-row { display: flex; align-items: center; gap: 7px; white-space: nowrap; }
  .footer-row.indent { padding-left: 16px; }
  .icon { width: 10px; height: 10px; flex: none; }
</style>
</head>
<body>
  <main class="letterhead">
    <div class="brand"><span class="brand-dot"></span>DORIAN WELK</div>

    <div class="credentials">
      <p class="credentials-name">DORIAN WELK NATUROPATH</p>
      <p class="credentials-line">Bachelor of Health Science</p>
      <p class="credentials-line">Adv. Dip. Naturophaty</p>
    </div>

    <div class="leaf-art" role="img" aria-label="Decorative translucent peach leaves"></div>

    <footer class="footer">
      <div class="footer-col">
        <div class="footer-row">
          <svg class="icon" viewBox="0 0 10 10"><path d="M5 0.5a3.5 3.5 0 0 0-3.5 3.5C1.5 6.6 5 9.8 5 9.8S8.5 6.6 8.5 4A3.5 3.5 0 0 0 5 0.5zm0 4.8A1.3 1.3 0 1 1 5 2.7a1.3 1.3 0 0 1 0 2.6z" fill="currentColor"/></svg>
          Dorian Welk Naturopath
        </div>
        <div class="footer-row indent">Shop 4123c, 46 Carrow Lane, Sydney 2000</div>
      </div>
      <div class="footer-col">
        <div class="footer-row">
          <svg class="icon" viewBox="0 0 10 10"><path d="M1 3.5C1 2 3 1.5 5 1.5S9 2 9 3.5v1H7v-1H3v1H1z M2.5 5h5l1 3.5h-7z" fill="currentColor"/></svg>
          0491 570 156
        </div>
        <div class="footer-row">
          <svg class="icon" viewBox="0 0 10 10"><rect x="0.8" y="2" width="8.4" height="6" fill="none" stroke="currentColor"/><path d="M1 2.3L5 5.5 9 2.3" fill="none" stroke="currentColor"/></svg>
          dwnaturopath@mailbox.com
        </div>
      </div>
      <div class="footer-col">
        <div class="footer-row">
          <svg class="icon" viewBox="0 0 10 10"><circle cx="5" cy="5" r="4.2" fill="none" stroke="currentColor"/><ellipse cx="5" cy="5" rx="1.8" ry="4.2" fill="none" stroke="currentColor"/><path d="M0.8 5h8.4" stroke="currentColor"/></svg>
          dorianwelk.com.au
        </div>
        <div class="footer-row">
          <svg class="icon" viewBox="0 0 10 10"><circle cx="5" cy="5" r="4.2" fill="none" stroke="currentColor"/><ellipse cx="5" cy="5" rx="1.8" ry="4.2" fill="none" stroke="currentColor"/><path d="M0.8 5h8.4" stroke="currentColor"/></svg>
          verdalessences.com.au
        </div>
      </div>
    </footer>
  </main>
</body>
</html>
```